Business card representing 2 natural foods companies!

Would love a business card that represents the 2 companies that I manage, PulpNova and Mirefield Crisp Leaf Co. Clearly, they are both premium food brands that have a cool, modern but classic feel.
I'm open to ideas for how to represent on 1 business card that I am Founder and President of both companies.
Contact Information for Business Card
Logos for both brands, and I think the most important thing is 2 different websites for each company (and perhaps 2 different emails for both companies)
sippulpnova.example
tobin@sippulpnova.example
mirefieldcrispleaf.example
tobin@mirefieldcrispleaf.example
Address isn't needed. I think phone number is good:
just cell: 555-014-7738
Also thinking is it possible to include a black LinkedIn QR code? I think that would be really cool to include.
Look and feel
Each slider illustrates characteristics of the customer's brand and the style your logo design should communicate.

```html
<!DOCTYPE html>
<html lang="en">
<head>
<meta charset="utf-8">
<title>Business Card — Mirefield Crisp Leaf Co. &amp; PulpNova</title>
<link rel="stylesheet" href="https://fonts.googleapis.com/css2?family=Exo+2:wght@400;500;600;700&display=swap">
<style>
  :root {
    --bg: #e4e2de;
    --card: #ffffff;
    --ink: #1f1f1f;
    --band: #222222;
    --white: #ffffff;
    --radius: 24px;
  }
  * { box-sizing: border-box; margin: 0; padding: 0; }
  html, body {
    width: 1200px; height: 1200px; overflow: hidden;
    background: var(--bg);
    font-family: "Exo 2", sans-serif;
    color: var(--ink);
  }
  .card {
    position: absolute;
    left: 148px; width: 904px; height: 516px;
    background: var(--card);
    border-radius: var(--radius);
    overflow: hidden;
    box-shadow: 0 18px 30px rgba(0,0,0,0.12);
  }
  .card--front { top: 32px; }
  .card--back { top: 621px; height: 519px; }

  /* front */
  .brand-mark {
    position: absolute; left: 100px; top: 226px; width: 330px; height: 136px;
    display: flex; align-items: center; justify-content: center; gap: 16px;
  }
  .brand-mark__dot {
    flex: none; width: 24px; height: 24px; border-radius: 50%;
    background: var(--ink);
  }
  .brand-mark__name {
    font-size: 32px; font-weight: 600; line-height: 1.15; color: var(--ink);
  }
  .title-band {
    position: absolute; left: 440px; top: 206px; width: 464px; height: 174px;
    background: linear-gradient(to right, rgba(34,34,34,0) 0%, rgba(34,34,34,0.55) 35%, var(--band) 75%);
    color: var(--white); text-align: right; padding: 55px 64px 0 0;
  }
  .title-band__name { font-size: 35px; font-weight: 500; letter-spacing: 1.5px; line-height: 1; }
  .title-band__role { font-size: 21px; font-weight: 400; letter-spacing: 1px; margin-top: 14px; }

  /* back */
  .wordmark {
    position: absolute; left: 64px; top: 62px;
    font-size: 76px; font-weight: 700; letter-spacing: 2px; line-height: 1; color: var(--ink);
  }
  .person { position: absolute; left: 64px; top: 258px; }
  .person__name { font-size: 35px; font-weight: 600; letter-spacing: 1.5px; line-height: 1; }
  .person__role { font-size: 21px; letter-spacing: 1px; margin-top: 8px; }
  .divider { position: absolute; left: 64px; top: 339px; width: 780px; height: 2px; background: var(--ink); }
  .contacts { position: absolute; left: 64px; top: 358px; list-style: none; font-size: 21px; letter-spacing: 0.8px; }
  .contacts li { display: flex; align-items: center; height: 29px; }
  .contacts svg { width: 16px; height: 16px; margin: 0 14px 0 3px; fill: var(--ink); }
  .address {
    position: absolute; right: 62px; top: 356px; text-align: right;
    font-size: 21px; letter-spacing: 0.8px; line-height: 31px;
  }
  .footer-bands { position: absolute; left: 0; top: 0; width: 904px; height: 519px; }
  .website {
    position: absolute; right: 62px; top: 481px;
    color: var(--white); font-size: 20px; letter-spacing: 1.2px;
  }
</style>
</head>
<body>

<section class="card card--front">
  <div class="brand-mark">
    <span class="brand-mark__dot"></span>
    <span class="brand-mark__name">Mirefield<br>Crisp Leaf Co.</span>
  </div>
  <div class="title-band">
    <p class="title-band__name">TOBIN HALE</p>
    <p class="title-band__role">Founder &amp; President</p>
  </div>
</section>

<section class="card card--back">
  <p class="wordmark">PulpNova</p>

  <div class="person">
    <p class="person__name">TOBIN HALE</p>
    <p class="person__role">Founder &amp; President</p>
  </div>
  <div class="divider"></div>

  <ul class="contacts">
    <li><svg viewBox="0 0 16 16"><rect x="3" y="0" width="10" height="16" rx="2"/><rect x="5" y="2" width="6" height="7" fill="#fff"/></svg>555 014 7738</li>
    <li><svg viewBox="0 0 16 16"><rect x="0" y="3" width="16" height="11" rx="1"/><path d="M1 4l7 5 7-5" stroke="#fff" stroke-width="1.5" fill="none"/></svg>tobin@mirefieldcrispleaf.example</li>
    <li><svg viewBox="0 0 16 16"><rect x="0" y="3" width="16" height="11" rx="1"/><path d="M1 4l7 5 7-5" stroke="#fff" stroke-width="1.5" fill="none"/></svg>tobin@sippulpnova.example</li>
  </ul>

  <p class="address">mirefieldcrispleaf.example<br>48210 Larkspur Way Ste. B<br>Brenton, OR 97702</p>

  <svg class="footer-bands" viewBox="0 0 904 519" aria-hidden="true">
    <polygon points="0,495 476,495 456,519 0,519" fill="var(--band)"/>
    <polygon points="508,473 904,473 904,519 464,519" fill="var(--band)"/>
  </svg>
  <p class="website">www.sippulpnova.example</p>
</section>

</body>
</html>
```